依頼詳細
トップページのデザイン トップページとサブページ(2ページ目以降)のデザイン サブページは、トップページのデザインを引き継ぐ感じで
グローバルナビ  ワードプレス×レスポンシブで制作予定

全体的なイメージ https://www.morino-kobo.jp/index.html
青とホワイトを基調にした清潔感があり ごちゃごちゃしすぎず
患者さんの視線で見やすく 探しやすい感じを希望します。
お子様や女性にも好まれるような可愛いイラストなどもお願いします。

グローバルナビに入れる予定の項目 Q&A、アクセス、医院紹介、治療内容、マウスピース矯正、費用、部分矯正、裏側矯正

トップページに記載したい文章
マウスピース型矯正装置(クリアフィット)をメインの紹介するサイト
裏側矯正にも力入れており、見えないMIX (マウスピース矯正と裏側矯正の組み合わせで幅広く対応できる。

最新式 デジタルスキャナー dento scope の紹介
参考https://hanawa-dent.jp/orthodontic/clearfit/

ブログ形式で 新着情報
休診日・診療時間/
ご相談・お問い合わせ

希望イメージ
シンプル 複雑
単色 カラフル
暗い 明るい
日常 高級
遊び心 厳粛
未来的 伝統的
女性的 男性的
希望する色
水色系
納品ファイル
• 高解像度JPG (.jpg)
• フォトショップ形式 (.psd)
補足説明
マウスピース矯正を マウスピース型矯正装置
クリアフィット をマウスピース型矯正装置(クリアフィット)

※医療広告の関係で表記を統一してください。
用語は、マウスピース型矯正装置(クリアフィット)を徹底してください。

高校生~20代女性に響くような デザインが希望です。

透明で見ないこと 取り外せること
最新式 3Dスキャンナー dento scoopeを導入していること
dento scope により、簡易シュミレーションが見れること
裏側矯正も得意なことから 組み合わせることによって対応できる
幅が広がったこと。

を強調したデザインが希望です。

参照https://www.kirari-ha.jp/simulation/

なるべく裏側矯正の内容は、記載しないでマウスピース型矯正装置(クリアフィット)の内容だけにしたい。

よろしくお願いします。

```html
<!DOCTYPE html>
<html lang="ja">
<head>
<meta charset="UTF-8">
<title>日本橋さくら通り矯正歯科</title>
<link href="https://fonts.googleapis.com/css2?family=Noto+Sans+JP:wght@300;400;500;700&family=Noto+Serif+JP:wght@400;500&display=swap" rel="stylesheet">
<style>
:root{
  --navy:#1c3f86;
  --blue:#2a6fc0;
  --sky:#5fbde9;
  --sky-pale:#dff2fb;
  --band-top:#7fcbef;
  --band-bottom:#d6f0fb;
  --ink:#333c4a;
  --muted:#6b7585;
  --line:#d8e3ee;
  --white:#ffffff;
  --card:#f6f9fc;
}
*{margin:0;padding:0;box-sizing:border-box}
html,body{width:1200px;height:4480px;overflow:hidden}
body{font-family:"Noto Sans JP",sans-serif;color:var(--ink);background:var(--white);position:relative}
.abs{position:absolute}
.ph{position:absolute}
/* header */
.site-header{position:absolute;top:0;left:0;width:1200px;height:96px;z-index:3}
.logo{position:absolute;left:40px;top:30px;font-family:"Noto Serif JP",serif;font-size:24px;font-weight:500;color:var(--navy);letter-spacing:.04em}
.gnav{position:absolute;right:40px;top:34px;display:flex;gap:22px;font-size:13px;color:var(--navy)}
/* hero */
.hero{position:absolute;top:0;left:0;width:1200px;height:680px;overflow:hidden}
.hero-photo{position:absolute;inset:0;background:linear-gradient(100deg,#ffffff 0%,#f3f8fc 38%,#e4edf3 60%,#d9c9bd 80%,#c8d8e6 100%)}
.hero-copy{position:absolute;left:0;width:760px;top:118px;text-align:center;color:var(--navy)}
.hero-copy .lead{font-size:38px;font-weight:500;letter-spacing:.06em}
.hero-copy h1{font-size:56px;font-weight:700;letter-spacing:.04em;line-height:1.3;margin-top:6px}
.hero-copy .paren{font-size:46px;font-weight:700}
.hero-copy .sub{font-size:15px;color:var(--sky);margin-top:30px;letter-spacing:.05em}
/* intro */
.intro-photo{left:0;top:670px;width:360px;height:380px;background:radial-gradient(ellipse at 40% 50%,#eef5fb 0%,#dbe7f1 55%,#ffffff 100%)}
.sec-title{font-size:26px;font-weight:500;color:var(--navy);letter-spacing:.05em}
.intro-title{left:520px;top:712px}
.intro-text{left:250px;top:778px;width:700px;font-size:13px;line-height:2;text-align:center;color:var(--muted)}
.side-photo{left:0;top:1190px;width:240px;height:420px;background:linear-gradient(90deg,#e9e1da 0%,#f3eee9 60%,#ffffff 100%)}
/* merit cards */
.merits{left:240px;top:930px;width:780px;display:grid;grid-template-columns:repeat(3,1fr);gap:20px}
.merit{height:270px;background:var(--card);border:1px solid var(--line);border-radius:6px;text-align:center;padding-top:24px;box-shadow:0 4px 14px rgba(40,90,150,.08)}
.merit .badge{display:inline-block;font-size:11px;color:var(--white);background:var(--sky);padding:2px 12px;border-radius:2px}
.merit .thumb{width:96px;height:96px;border-radius:50%;margin:14px auto 14px;background:radial-gradient(circle,#f4ede7 0%,#cfe1ee 100%)}
.merit h3{font-size:20px;font-weight:500;color:var(--navy)}
.merit p{font-size:11px;color:var(--muted);line-height:1.8;margin:10px 26px 0}
.btn{position:absolute;display:flex;align-items:center;justify-content:center;width:270px;height:50px;border-radius:25px;background:var(--navy);color:var(--white);font-size:15px;letter-spacing:.08em}
/* scanner */
.scan-name{left:140px;top:1790px;font-size:40px;font-weight:500;color:var(--navy);letter-spacing:.02em}
.scan-device{left:470px;top:1790px;width:620px;height:400px;background:linear-gradient(180deg,#f2f6f9 0%,#dfe6ec 100%);border-radius:8px}
.scan-cart{left:330px;top:1830px;width:130px;height:360px;background:linear-gradient(180deg,#e8edf1 0%,#cfd7de 100%);border-radius:8px}
.bubble{left:880px;top:1800px;width:170px;height:110px;background:var(--white);border:2px solid var(--sky);border-radius:50%;display:flex;align-items:center;justify-content:center;text-align:center;font-size:12px;line-height:1.6;color:var(--navy)}
.chara{left:990px;top:1860px;width:100px;height:110px;border-radius:50%;background:#fde6d6}
/* band */
.band{left:0;top:2200px;width:1200px;height:720px;background:linear-gradient(180deg,var(--band-top) 0%,var(--band-bottom) 55%,#ffffff 100%)}
.band-title{left:0;width:1200px;top:2298px;text-align:center;color:var(--white);font-size:26px;font-weight:500;letter-spacing:.05em}
.band-text{left:260px;width:680px;top:2356px;text-align:center;font-size:13px;line-height:2;color:var(--white)}
.points{left:120px;top:2480px;width:960px;display:grid;grid-template-columns:repeat(3,1fr);gap:36px}
.point{height:360px;background:var(--white);border-radius:4px;text-align:center;padding-top:40px;box-shadow:0 6px 20px rgba(40,110,170,.14)}
.point .icon{width:90px;height:90px;margin:0 auto 28px;border-radius:10px;background:var(--sky-pale)}
.point h3{font-size:20px;font-weight:500;color:var(--navy)}
.point p{font-size:12px;color:var(--muted);line-height:1.9;margin:16px 30px 0;text-align:left}
/* lingual */
.lingual-photo{left:280px;top:3020px;width:400px;height:350px;background:linear-gradient(135deg,#f4f6f8 0%,#dde3e8 100%)}
.lingual-title{left:700px;top:3060px;font-size:24px}
.lingual-text{left:700px;top:3120px;width:380px;font-size:14px;line-height:1.8;color:var(--ink)}
.lingual-small{left:700px;top:3190px;width:380px;font-size:11px;line-height:1.9;color:var(--muted)}
/* info panels */
.info{left:0;top:3480px;width:1200px;height:520px;background:linear-gradient(180deg,#ffffff 0%,var(--sky-pale) 100%)}
.panel{top:3530px;height:430px;background:var(--white);border-radius:4px;box-shadow:0 4px 16px rgba(40,90,150,.1)}
.panel-news{left:140px;width:440px}
.panel-hours{left:620px;width:520px}
.panel-head{display:flex;align-items:center;gap:12px;height:60px;padding-left:22px;background:var(--sky-pale);font-size:20px;font-weight:500;color:var(--navy)}
.panel-head .mark{width:28px;height:28px;border-radius:50%;background:var(--sky)}
.panel-head .mark.sq{border-radius:4px;background:var(--navy)}
.news{list-style:none;margin:26px 28px 0}
.news li{display:flex;gap:26px;font-size:13px;padding:18px 0;border-bottom:1px dotted var(--line)}
.news time{color:var(--muted)}
.hours{margin:26px 24px 0;width:472px;border-collapse:collapse;font-size:13px;text-align:center}
.hours th,.hours td{border-bottom:1px solid var(--line);padding:14px 0}
.hours thead th{background:#f1f6fb;color:var(--navy);font-weight:500}
.hours td.time{text-align:left;padding-left:10px}
.hours .mark-o{color:var(--sky)}
.hours-note{margin:16px 24px;font-size:12px;color:var(--muted);line-height:1.8}
/* footer */
.footer{left:0;top:4000px;width:1200px;height:380px;background:linear-gradient(90deg,#ffffff 0%,#f2f7fb 45%,#e6edf3 100%)}
.foot-name{left:140px;top:4040px;font-family:"Noto Serif JP",serif;font-size:26px;color:var(--navy)}
.foot-addr{left:140px;top:4100px;font-size:12px;line-height:1.9;color:var(--muted)}
.contact{left:480px;top:4150px;width:640px;height:110px;background:var(--white);border:1px solid var(--line);display:flex;align-items:center;padding-left:30px;gap:24px}
.contact .tel-label{font-size:13px;color:var(--navy)}
.contact .tel{font-size:30px;font-weight:700;color:var(--navy);display:flex;align-items:center;gap:8px}
.cbtn{width:150px;height:44px;border:1px solid var(--navy);color:var(--navy);font-size:12px;display:flex;align-items:center;justify-content:center}
.bottom{left:0;top:4380px;width:1200px;height:100px;background:var(--sky);color:var(--white)}
.bottom nav{position:absolute;right:40px;top:28px;display:flex;gap:24px;font-size:12px}
.bottom small{position:absolute;right:40px;top:62px;font-size:11px}
</style>
</head>
<body>

<section class="hero">
  <div class="hero-photo" role="img" aria-label="透明なマウスピース型矯正装置を手に持ち微笑む女性の写真"></div>
  <div class="hero-copy">
    <p class="lead">透明で目立たない</p>
    <h1>マウスピース型矯正装置<br><span class="paren">(クリアフィット)</span></h1>
    <p class="sub">取り外せて目立たない、新しい矯正治療をはじめませんか。</p>
  </div>
</section>

<header class="site-header">
  <div class="logo">日本橋さくら通り矯正歯科</div>
  <nav class="gnav">
    <span>マウスピース型矯正装置</span><span>医院紹介</span><span>治療内容</span><span>部分矯正</span><span>裏側矯正</span><span>費用</span><span>アクセス</span><span>Q&amp;A</span>
  </nav>
</header>

<div class="ph intro-photo" role="img" aria-label="透明なマウスピースの写真"></div>
<h2 class="abs sec-title intro-title">マウスピース型矯正装置(クリアフィット)</h2>
<p class="abs intro-text">マウスピース型矯正装置(クリアフィット)は、透明なマウスピースを使用した新しい矯正治療です。<br>装置が目立ちにくく、取り外しができるため、食事や歯みがきもこれまで通り行えます。<br>お一人おひとりの歯並びに合わせて、段階的に作製したマウスピースを交換しながら<br>少しずつ理想の歯並びへと近づけていきます。</p>
<div class="ph side-photo" role="img" aria-label="マウスピースを装着する女性の写真"></div>

<div class="abs merits">
  <div class="merit"><span class="badge">メリット1</span><div class="thumb" role="img" aria-label="口元の写真"></div><h3>見た目に目立たない</h3><p>透明な素材のため装着していても周りの人に気付かれにくいです。</p></div>
  <div class="merit"><span class="badge">メリット2</span><div class="thumb" role="img" aria-label="食事の写真"></div><h3>取り外して、食事ができる</h3><p>食事の時は外せるので、好きなものを気にせず召し上がれます。</p></div>
  <div class="merit"><span class="badge">メリット3</span><div class="thumb" role="img" aria-label="歯みがきの写真"></div><h3>むし歯のリスクが減る</h3><p>外して歯みがきができるため、お口を清潔に保てます。</p></div>
  <div class="merit"><span class="badge">メリット4</span><div class="thumb" role="img" aria-label="マウスピースの写真"></div><h3>金属アレルギーの心配がない</h3><p>金属を使用しないので、アレルギーのある方も安心です。</p></div>
  <div class="merit"><span class="badge">メリット5</span><div class="thumb" role="img" aria-label="笑顔の口元の写真"></div><h3>痛みが少ない</h3><p>少しずつ歯を動かすため、痛みや違和感が少なく済みます。</p></div>
  <div class="merit"><span class="badge">メリット6</span><div class="thumb" role="img" aria-label="口腔内スキャナの写真"></div><h3>最新3Dスキャナー使用</h3><p>型取りの不快感がなく、精密なデータで治療計画を立てます。</p></div>
</div>
<a class="btn" style="left:465px;top:1676px">view more</a>

<div class="abs scan-name">dento scope<span style="font-size:16px;vertical-align:top;color:var(--sky)"> ●</span></div>
<div class="ph scan-cart" role="img" aria-label="スタンド型口腔内スキャナの写真"></div>
<div class="ph scan-device" role="img" aria-label="歯列の3D画像を表示するスキャナ本体とモニターの写真"></div>
<div class="abs bubble">口腔内を撮影するだけ<br>で、3D画像がすぐに<br>見られます!</div>
<div class="ph chara" role="img" aria-label="歯科衛生士のイラスト"></div>

<div class="abs band"></div>
<h2 class="abs band-title">dento scope(口腔内スキャナ)</h2>
<p class="abs band-text">dento scopeは、お口の中を小型カメラでスキャンするだけで歯並びの3Dデータを作成する装置です。<br>従来の粘土のような型取りが不要になり、短時間で精密な記録が可能になりました。<br>スキャン後はその場で治療後のシミュレーションをご覧いただけます。</p>
<div class="abs points">
  <div class="point"><div class="icon" role="img" aria-label="モニターのイラスト"></div><h3>精密データの取得</h3><p>歯や歯ぐきの形を細部まで正確に読み取り、ずれの少ない精密なデータを取得できます。</p></div>
  <div class="point"><div class="icon" role="img" aria-label="時計のイラスト"></div><h3>スピーディな治療</h3><p>データをすぐに送信できるため、装置の作製までの期間が短くなり、スムーズに治療を始められます。</p></div>
  <div class="point"><div class="icon" role="img" aria-label="笑顔の人物のイラスト"></div><h3>快適</h3><p>型取り材を使わないので、嘔吐反射や息苦しさがなく、快適に検査を受けていただけます。</p></div>
</div>
<a class="btn" style="left:465px;top:2890px">view more</a>

<div class="ph lingual-photo" role="img" aria-label="歯列模型とマウスピースの写真"></div>
<h2 class="abs sec-title lingual-title">裏側矯正</h2>
<p class="abs lingual-text">マウスピース型矯正装置と裏側矯正の組み合わせで<br>幅広く対応できます。</p>
<p class="abs lingual-small">見えない装置同士を組み合わせることで、これまで難しかった症例にも対応できるようになりました。お気軽にご相談ください。</p>
<a class="btn" style="left:700px;top:3400px;width:200px;height:44px">view more</a>

<div class="abs info"></div>
<section class="abs panel panel-news">
  <div class="panel-head"><span class="mark"></span>お知らせ</div>
  <ul class="news">
    <li><time>2018.12.15</time><span>年末年始の休診日のお知らせ</span></li>
    <li><time>2018.12.15</time><span>無料カウンセリングのご案内</span></li>
    <li><time>2018.12.15</time><span>ホームページを公開しました</span></li>
  </ul>
  <a class="btn" style="position:absolute;left:220px;top:350px;width:180px;height:40px;font-size:13px">view more</a>
</section>
<section class="abs panel panel-hours">
  <div class="panel-head"><span class="mark sq"></span>診療時間</div>
  <table class="hours">
    <thead><tr><th>診療時間</th><th>月</th><th>火</th><th>水</th><th>木</th><th>金</th><th>土</th><th>日</th></tr></thead>
    <tbody>
      <tr><td class="time">10:00〜13:00</td><td class="mark-o">○</td><td class="mark-o">○</td><td>/</td><td class="mark-o">○</td><td class="mark-o">○</td><td class="mark-o">○</td><td>/</td></tr>
      <tr><td class="time">14:00〜19:00</td><td class="mark-o">○</td><td class="mark-o">○</td><td>/</td><td class="mark-o">○</td><td class="mark-o">○</td><td class="mark-o">○</td><td>/</td></tr>
    </tbody>
  </table>
  <p class="hours-note">休診日:水曜・日曜・祝日<br>※土曜日は17:00まで</p>
</section>

<div class="ph footer" role="img" aria-label="やわらかくぼかした医院内の写真"></div>
<div class="abs foot-name">日本橋さくら通り矯正歯科</div>
<p class="abs foot-addr">〒103-0000<br>東京都中央区日本橋さくら通り1-2-3 2F<br>診療時間<br>10:00〜13:00 / 14:00〜19:00<br>休診日<br>水曜日・日曜日・祝日</p>
<div class="abs contact">
  <div>
    <p class="tel-label">お気軽にお問い合わせください</p>
    <p class="tel"><svg width="24" height="24" viewBox="0 0 24 24"><path d="M6.6 10.8c1.4 2.8 3.8 5.1 6.6 6.6l2.2-2.2c.3-.3.7-.4 1-.2 1.1.4 2.3.6 3.6.6.6 0 1 .4 1 1V20c0 .6-.4 1-1 1C10.6 21 3 13.4 3 4c0-.6.4-1 1-1h3.5c.6 0 1 .4 1 1 0 1.3.2 2.5.6 3.6.1.3 0 .7-.2 1z" fill="#1c3f86"/></svg>03-5550-2841</p>
  </div>
  <div class="cbtn">ご相談・お問い合わせ</div>
  <div class="cbtn">無料カウンセリング予約</div>
</div>

<footer class="abs bottom">
  <nav><span>マウスピース型矯正装置</span><span>医院紹介</span><span>治療内容</span><span>部分矯正</span><span>裏側矯正</span><span>費用</span><span>アクセス</span><span>Q&amp;A</span><span>お知らせ</span></nav>
  <small>Copyright © Sakuradori Orthodontics All Rights Reserved.</small>
</footer>

</body>
</html>
```